New modern and colorful Brochure for Real Estate shop window/showcase

We are a real estate company in the swiss alps and we need a new design for our (very old fashioned) brochures. Our “word-doc” based “brochure” you’ll find in the attachment.

We need a whole new, modern, clean and colorful design. The key features of a property must be clearly visible, like: (Those key features must be editable)

- 1 main bigger picture of the property
- 4-6 small accompagning Fotos
- Floorplan
- Price
- Property Category
- Buildyear
- Number of rooms
- Number of bathrooms
- Number of bedrooms
- Squaremeter
- Parking place
- Specialities
- Very Short Descripton of the property

We put those brochures in our shop window/showcase, see foto in the attachment. In the attachment you’ll find our business card logo, letterhead logo and on our website www.halvormark-ag.ch another logo.

The new brochure will contain about 4-6 pictures with a main picture of the house, a floorplan and a short description. It must be clearly visible und readable from outside thru a window, so it canot be too small.

Format only A3 in LANDSCAPE.

It must be scalable to A4 to be able to send it to clients (and they will print it to A4)

The brochure must contain our logo with name, subname and year, website, telefon and fax number and address.

To be clear: The whole new brochure will contain only a short description, not like the old design. You can really more concentrate on design and fotos. Description and text will be very short. But we really want to change and no more using the old design...

Just to clarify, the picture with our little agency is just for reference where the new brochures will be. It's jus there to show our window/showcase.

Hope you can help us. Many Greetings and thank you from us!

Project Deadline Extended Reason: Not yet found/submitted "the one". We are missing a more central/important position of the key features of a property. They must be really clearly seen from outside of the window. And we need a two sided A4 "light" version, to hand out to clients. We can't give them a big A3 paper. Scaled down thru the printer isn't the best option. I light version would be optimal....Please continue to submit designs and adopt to the new task, we will reply and give immediate feedback. Thanks a lot! Added Tuesday, January 31, 2017

Reason: still not found the right one

Target Market(s)

Real Estate, Shop Window, Showcase

Industry/Entity Type

Real Estate

Font styles to use
Sans Serif

Colors
0655a3
ec1f27
0293ce
ffc214
e34297

Requirements
Must have
• A3 Format landscape.
• - 1 main bigger picture of the property
• - 4-6 small accompagning Fotos
• - Floorplan
• - Price
• - Property Category
• - Buildyear
• - Number of rooms
• - Number of bathrooms
• - Number of bedrooms
• - Squaremeter
• - Parking place
• - Specialities
• - Short Descripton of the property

```html
<!DOCTYPE html>
<html lang="en">
<head>
<meta charset="utf-8">
<title>Halvormark AG – Property Flyer</title>
<link href="https://fonts.googleapis.com/css2?family=Open+Sans:ital,wght@0,400;0,600;0,700;1,400&family=Oswald:wght@400;500&display=swap" rel="stylesheet">
<style>
  :root{
    --bg:#e8e8e8;
    --paper:#ffffff;
    --brand-blue:#175b8c;
    --gold:#e6a01e;
    --ink-blue:#1f5f96;
    --text-light:#ffffff;
    --price-blue:#1c5b93;
  }
  *{box-sizing:border-box;margin:0;padding:0}
  html,body{width:1200px;height:800px;overflow:hidden;background:var(--bg);font-family:"Open Sans",Arial,sans-serif}
  .spread{position:relative;width:1200px;height:800px}
  .page{position:absolute;top:103px;width:420px;height:594px;background:var(--paper);overflow:hidden;box-shadow:0 6px 18px rgba(0,0,0,.18)}
  .page--front{left:150px}
  .page--back{left:630px}

  /* front */
  .hero{position:absolute;left:0;top:0;width:420px;height:318px;
    background:linear-gradient(160deg,#2748a3 0%,#3d64bd 40%,#c9b79a 62%,#8a4a2a 78%,#e9eef3 100%)}
  .brand{position:absolute;display:flex;align-items:center;gap:8px;color:var(--text-light);white-space:nowrap}
  .brand__mark{width:20px;height:20px;border-radius:50%;background:rgba(255,255,255,.85);flex:none}
  .brand__name{font-weight:600;font-size:15px;letter-spacing:.5px;line-height:1}
  .brand__sub{font-size:8.5px;opacity:.9;margin-top:3px}
  .hero .brand{right:18px;top:16px}

  .info-band{position:absolute;left:0;top:318px;width:420px;height:186px;background:var(--gold);padding:14px 16px;color:var(--text-light)}
  .features{display:grid;grid-template-columns:1fr 1.1fr 1.05fr;border:1.5px solid rgba(255,255,255,.9);font-family:"Oswald",Arial,sans-serif;font-size:12px;line-height:1.35}
  .features__cell{padding:5px 7px;border-right:1.5px solid rgba(255,255,255,.9)}
  .features__cell:last-child{border-right:none;padding:0}
  .features__category{font-size:14px}
  .price{background:var(--price-blue);padding:5px 7px;font-size:14px;font-weight:500}
  .parking{padding:4px 7px}
  .description{margin-top:10px;font-size:9.6px;line-height:1.45}
  .description strong{font-weight:700}

  .footer{position:absolute;left:0;bottom:0;width:420px;height:90px;background:var(--brand-blue);color:var(--text-light);display:flex;align-items:center;justify-content:space-between;padding:0 16px}
  .footer .brand{position:static}
  .contact{font-size:7.6px;line-height:1.7;text-align:right;white-space:nowrap}
  .contact b{font-weight:700}

  /* back */
  .top-band{position:absolute;left:0;top:0;width:420px;height:58px;background:var(--gold)}
  .floorplan{position:absolute;left:0;top:76px;width:190px;height:150px;background:linear-gradient(135deg,#f3f3f3,#dcdcdc)}
  .equipment{position:absolute;left:212px;top:76px;width:196px;color:var(--ink-blue)}
  .equipment__title{font-weight:700;font-size:10.5px;letter-spacing:.5px;margin-bottom:4px}
  .equipment__list{list-style:none;font-size:10.5px;line-height:1.35}
  .gallery{position:absolute;left:0;top:260px;width:420px;height:238px;display:grid;grid-template-columns:1.15fr 1fr;grid-template-rows:repeat(6,1fr);gap:6px}
  .photo{width:100%;height:100%}
  .photo--bedroom{grid-column:1;grid-row:1/4;background:linear-gradient(135deg,#e9d8c8,#b07a52)}
  .photo--living{grid-column:1;grid-row:4/7;background:linear-gradient(135deg,#d9c2a6,#7e4d2c)}
  .photo--bath{grid-column:2;grid-row:1/3;background:linear-gradient(135deg,#e6dccf,#a67b56)}
  .photo--kitchen{grid-column:2;grid-row:3/5;background:linear-gradient(135deg,#c99b6a,#6e4427)}
  .photo--view{grid-column:2;grid-row:5/7;background:linear-gradient(180deg,#5d86c4 0%,#9bb5d6 40%,#6e8f4a 75%,#8a7a68 100%)}
</style>
</head>
<body>
<div class="spread">

  <section class="page page--front">
    <div class="hero" role="img" aria-label="Main photograph of the chalet apartment building against a blue winter sky">
      <div class="brand">
        <span class="brand__mark"></span>
        <div><div class="brand__name">HALVORMARK AG</div><div class="brand__sub">Immobilien und Finanzierungen</div></div>
      </div>
    </div>

    <div class="info-band">
      <div class="features">
        <div class="features__cell">
          <div class="features__category">3-room apartment</div>
          <div>living area: 60 sqm</div>
        </div>
        <div class="features__cell">
          <div>year of construction: 1981</div>
          <div>bedrooms: 2</div>
          <div>bathrooms: 1</div>
        </div>
        <div class="features__cell">
          <div class="price">PRICE CHF 390 000</div>
          <div class="parking">parking: garage box</div>
        </div>
      </div>
      <p class="description"><strong>The House Alpina with only 4 apartments is located in a central south slope beside the Talstation.</strong> Bakery, restaurants, supermarkets etc. are in the immediate vicinity. The stop of the local ring bus is only 30m away from the building. The Alpina building was built in 1981 and is in a superbly maintained state. The 3-room apartment with about 60sqm usable area has a bright ground plan, is fully furnished and can be obtained immediately or by appointment.</p>
    </div>

    <footer class="footer">
      <div class="brand">
        <span class="brand__mark"></span>
        <div><div class="brand__name">HALVORMARK AG</div><div class="brand__sub">Immobilien und Finanzierungen</div></div>
      </div>
      <div class="contact">
        <div><b>3958 Brigwald</b> phone: +41 27 555 01 76 fax: +41 27 555 01 77</div>
        <div><b>www.halvormark-ag.ch</b> e-mail: <b>info@halvormark-ag.ch</b></div>
      </div>
    </footer>
  </section>

  <section class="page page--back">
    <div class="top-band"></div>
    <div class="floorplan" role="img" aria-label="Floor plan of the apartment with room, bathroom and bedroom"></div>
    <div class="equipment">
      <h3 class="equipment__title">GENERAL EQUIPMENT</h3>
      <ul class="equipment__list">
        <li>Lift / elevator</li>
        <li>Floor heating</li>
        <li>Unobstructed view</li>
        <li>Waiting / Concierge / Caretaker</li>
        <li>Cellar / storage room</li>
        <li>Balcony</li>
        <li>Garage box</li>
        <li>Central heating</li>
        <li>Fully furnished and equipped</li>
        <li>Exquisite furnishings</li>
      </ul>
    </div>
    <div class="gallery">
      <div class="photo photo--bedroom" role="img" aria-label="Photo of the bedroom"></div>
      <div class="photo photo--living" role="img" aria-label="Photo of the living and dining room"></div>
      <div class="photo photo--bath" role="img" aria-label="Photo of the wood-panelled bathroom"></div>
      <div class="photo photo--kitchen" role="img" aria-label="Photo of the kitchen"></div>
      <div class="photo photo--view" role="img" aria-label="Photo of the mountain village view"></div>
    </div>
    <footer class="footer">
      <div class="brand">
        <span class="brand__mark"></span>
        <div><div class="brand__name">HALVORMARK AG</div><div class="brand__sub">Immobilien und Finanzierungen</div></div>
      </div>
      <div class="contact">
        <div><b>3958 Brigwald</b> phone: +41 27 555 01 76 fax: +41 27 555 01 77</div>
        <div><b>www.halvormark-ag.ch</b> e-mail: <b>info@halvormark-ag.ch</b></div>
      </div>
    </footer>
  </section>

</div>
</body>
</html>
```